Blue Heron IT Business Card - Clean, Simple

Need a simple, clean standard sized business card for an IT consulting business using existing logo and company colours. Background should be mainly white. Feel free to be creative but clean, simple, quiet design is preferred. Font is specified in logo but any sans serif fonts work.

Contact Information for card is as follows (doesn't need to be in this exact order):

Martin Calloway
Owner
martin@blueheronit.ca
705-391-2586
www.blueheronit.ca

Target Market(s)

Small to medium sized business.

Industry/Entity Type

IT Consulting

Contact Information for Business Card

Logo and contact info.

Font styles to use
Sans Serif

Colors
EE7325
F08F49
F5BC92
FAE3D3
FDF4ED

Requirements
Must have
• All white or mostly white background.

```html
<!DOCTYPE html>
<html lang="en">
<head>
<meta charset="utf-8">
<title>Blue Heron IT — Business Card</title>
<link href="https://fonts.googleapis.com/css2?family=Raleway:wght@400;500;600;700&display=swap" rel="stylesheet">
<style>
  :root {
    --orange: #EE7325;
    --orange-light: #F08F49;
    --peach: #F5BC92;
    --charcoal: #3a3a3c;
    --ink: #3d3d3f;
    --white: #ffffff;
    --backdrop: #dfe3ea;
  }
  * { box-sizing: border-box; margin: 0; padding: 0; }
  html, body { width: 1200px; height: 876px; overflow: hidden; }
  body {
    background: var(--backdrop);
    font-family: "Raleway", sans-serif;
    display: flex;
    align-items: center;
    justify-content: center;
    gap: 40px;
  }
  .card {
    position: relative;
    width: 540px;
    height: 309px;
    overflow: hidden;
    box-shadow: 0 6px 18px rgba(40, 50, 70, 0.18);
  }

  /* Front side */
  .card--front { background: var(--white); }
  .side-band {
    position: absolute; left: 0; top: 0; bottom: 0;
    width: 46px;
    background: var(--charcoal);
  }
  .side-band__accent {
    position: absolute; left: 0; width: 46px;
    top: 212px; height: 34px;
    background: var(--orange);
  }
  .contact-list {
    position: absolute; left: 46px; top: 24px;
    list-style: none;
  }
  .contact-list li {
    display: flex; align-items: center;
    height: 28px;
    font-size: 15px; color: var(--ink);
    letter-spacing: 0.2px;
  }
  .contact-list .icon {
    width: 20px; height: 20px;
    margin-left: -34px; margin-right: 30px;
    flex: none;
  }
  .person {
    position: absolute; left: 64px; top: 216px;
    color: var(--ink);
  }
  .person__name {
    font-size: 17px; text-transform: uppercase; letter-spacing: 0.3px;
  }
  .person__name strong { font-weight: 700; }
  .person__name span { font-weight: 400; }
  .person__role {
    font-size: 11px; text-transform: uppercase; letter-spacing: 0.5px;
    margin-top: 1px;
  }
  .brand {
    position: absolute; right: 34px; top: 118px;
    display: flex; align-items: center; gap: 10px;
  }
  .brand__dot {
    width: 22px; height: 22px; border-radius: 50%;
    background: var(--orange);
  }
  .brand__name {
    font-size: 34px; font-weight: 600; color: var(--ink);
    letter-spacing: -0.3px;
  }
  .accent-bar {
    position: absolute; right: 0; top: 240px;
    width: 298px; height: 24px;
    background: linear-gradient(90deg, var(--orange-light), var(--orange));
  }

  /* Back side */
  .card--back {
    background: linear-gradient(125deg, var(--orange) 0%, var(--orange-light) 50%, var(--orange) 100%);
  }
  .back-brand {
    position: absolute; left: 0; right: 0; top: 104px;
    display: flex; align-items: center; justify-content: center; gap: 12px;
  }
  .back-brand .brand__dot { background: var(--white); width: 24px; height: 24px; }
  .back-brand .brand__name { color: var(--white); font-size: 40px; }
  .back-url {
    position: absolute; left: 0; right: 0; top: 176px;
    text-align: center;
    color: var(--white);
    font-size: 13px; font-weight: 600;
    letter-spacing: 7px;
  }
</style>
</head>
<body>

  <section class="card card--front" aria-label="Business card front">
    <div class="side-band"><div class="side-band__accent"></div></div>

    <ul class="contact-list">
      <li>
        <svg class="icon" viewBox="0 0 20 20" aria-hidden="true">
          <circle cx="10" cy="10" r="10" fill="var(--orange)"/>
          <rect x="5" y="6.5" width="10" height="7" rx="1" fill="none" stroke="#fff" stroke-width="1.4"/>
          <path d="M5.3 7 L10 10.8 L14.7 7" fill="none" stroke="#fff" stroke-width="1.4"/>
        </svg>
        martin@blueheronit.ca
      </li>
      <li>
        <svg class="icon" viewBox="0 0 20 20" aria-hidden="true">
          <circle cx="10" cy="10" r="10" fill="var(--orange)"/>
          <path d="M7 5.2 C6 5.6 5.4 6.6 5.8 8 C6.6 10.8 9.2 13.4 12 14.2 C13.4 14.6 14.4 14 14.8 13 L13 11.4 L11.7 12.3 C10.2 11.6 8.4 9.8 7.7 8.3 L8.6 7 Z" fill="#fff"/>
        </svg>
        705-391-2586
      </li>
      <li>
        <svg class="icon" viewBox="0 0 20 20" aria-hidden="true">
          <circle cx="10" cy="10" r="10" fill="var(--orange)"/>
          <circle cx="10" cy="10" r="5" fill="none" stroke="#fff" stroke-width="1.3"/>
          <ellipse cx="10" cy="10" rx="2.2" ry="5" fill="none" stroke="#fff" stroke-width="1.1"/>
          <line x1="5" y1="10" x2="15" y2="10" stroke="#fff" stroke-width="1.1"/>
        </svg>
        www.blueheronit.ca
      </li>
    </ul>

    <div class="person">
      <p class="person__name"><strong>Martin</strong><span>Calloway</span></p>
      <p class="person__role">Owner</p>
    </div>

    <div class="brand">
      <span class="brand__dot"></span>
      <span class="brand__name">Blue Heron IT</span>
    </div>

    <div class="accent-bar"></div>
  </section>

  <section class="card card--back" aria-label="Business card back">
    <div class="back-brand">
      <span class="brand__dot"></span>
      <span class="brand__name">Blue Heron IT</span>
    </div>
    <p class="back-url">www.blueheronit.ca</p>
  </section>

</body>
</html>
```